"Wellenhafen" private practice for physiotherapy

we are looking for a flyer design for a private practice for physiotherapy. the name of the practice is "Wellenhafen".
Treatments such as: manual therapy, manual lymphatic drainage, classic massage, sectoral alternative practitioners are offered

The flyers should be double-sided and the format DIN long (105x210 mm)

Font styles to use
Serif

Colors
0094D4
00A9DD
6FCCEA
C7EBF8
E9F6FB

Requirements
Must have
• Wellenhafen, Lindenweg 17, 04719 Talbrück / Wellenhafen-praxis-beispiel.de / Tel. 03471 5820317

```html
<!DOCTYPE html>
<html lang="en">
<head>
<meta charset="utf-8">
<title>Wellenhafen – Physiotherapy Flyer</title>
<link rel="stylesheet" href="https://fonts.googleapis.com/css2?family=Cinzel:wght@500;700&display=swap">
<style>
  :root{
    --blue:#0094D4;
    --blue-deep:#1f95d6;
    --blue-bright:#00A9DD;
    --blue-soft:#6FCCEA;
    --blue-pale:#C7EBF8;
    --blue-mist:#E9F6FB;
    --white:#ffffff;
    --serif:"Cinzel", Georgia, serif;
  }
  *{margin:0;padding:0;box-sizing:border-box}
  html,body{width:826px;height:1200px;overflow:hidden}
  body{background:var(--blue-mist);font-family:var(--serif);position:relative}
  .side-label{position:absolute;top:196px;width:370px;text-align:center;
    font-size:16px;letter-spacing:1px;color:var(--blue);font-weight:500}
  .side-label.front{left:30px}
  .side-label.back{left:426px}
  .flyer{position:absolute;top:230px;width:370px;height:740px;background:var(--white);overflow:hidden}
  .flyer.front{left:30px}
  .flyer.back{left:426px}
  .stripe{position:absolute;left:0;width:100%;background:var(--blue)}
  .abs{position:absolute;left:0;width:100%}
  .photo{position:absolute;left:0;width:100%}
  .front .photo{top:90px;height:400px;
    background:radial-gradient(ellipse at 48% 55%, #a9d3ea 0%, #dcedf7 40%, #ffffff 70%)}
  .back .photo{top:8px;height:360px;
    background:linear-gradient(160deg,#4fb5e8 0%,#2a9ad8 45%,#bfe2f4 100%)}
  .brand{position:absolute;top:6px;left:0;width:100%;height:64px;display:flex;
    align-items:center;justify-content:center;color:var(--white);
    font-size:29px;font-weight:700;letter-spacing:1px}
  .headline{position:absolute;top:538px;left:0;width:100%;text-align:center;
    color:var(--white);font-size:25px;font-weight:700;line-height:1.25;letter-spacing:.5px}
  .headline .for{display:inline-block;background:var(--blue-pale);color:var(--blue-bright);
    padding:0 12px;margin:2px 0;line-height:1.05}
  .phone{position:absolute;top:668px;left:0;width:100%;height:67px;display:flex;
    align-items:center;justify-content:center;gap:10px;color:var(--blue);font-size:32px;font-weight:500}
  .phone svg{width:22px;height:30px}
  .services{position:absolute;top:425px;left:16px;list-style:none;color:var(--white);
    font-size:16px;font-weight:700;letter-spacing:.3px}
  .services li{position:relative;padding-left:14px;margin-bottom:20px;line-height:1.3}
  .services li::before{content:"";position:absolute;left:0;top:8px;width:6px;height:6px;
    border-radius:50%;background:var(--blue-pale)}
  .services li span{display:inline-block;border-bottom:2px solid var(--blue-pale);padding-bottom:2px}
  .contact{position:absolute;top:688px;left:16px;color:var(--blue);font-size:8.5px;
    font-weight:500;line-height:1.9}
  .contact div{display:flex;align-items:center;gap:6px}
  .contact svg{width:8px;height:9px}
</style>
</head>
<body>
  <div class="side-label front">FRONT SIDE</div>
  <div class="side-label back">BACK SIDE</div>

  <section class="flyer front">
    <div class="stripe" style="top:0;height:6px;background:var(--blue-soft)"></div>
    <svg class="abs" style="top:6px" width="370" height="84" viewBox="0 0 370 84">
      <path d="M0 0H370V64Q185 78 0 64Z" fill="#1f95d6"/>
      <path d="M20 76Q185 66 350 76" stroke="var(--blue-pale)" stroke-width="3" fill="none"/>
    </svg>
    <div class="brand">WELLENHAFEN</div>
    <div class="photo" role="img" aria-label="Photo of a physiotherapist guiding a patient through a shoulder stretch"></div>
    <svg class="abs" style="top:480px" width="370" height="190" viewBox="0 0 370 190">
      <path d="M0 18Q185 0 370 18V190H0Z" fill="#1f95d6"/>
      <path d="M0 18Q185 0 370 18" stroke="var(--blue-soft)" stroke-width="3" fill="none"/>
      <path d="M20 182Q185 170 350 182" stroke="var(--blue-pale)" stroke-width="3" fill="none"/>
    </svg>
    <div class="headline">PRIVATE PRACTICE<br><span class="for">FOR</span><br>PHYSIOTHERAPY</div>
    <div class="stripe" style="top:668px;height:67px;background:var(--blue-pale)"></div>
    <div class="phone">
      <svg viewBox="0 0 22 30"><path d="M6 1L10 8 7 11Q9 19 14 22L17 19 21 25 16 29Q9 28 4 18T2 4Z" fill="var(--blue)"/></svg>
      03471 5820317
    </div>
    <div class="stripe" style="top:735px;height:5px"></div>
  </section>

  <section class="flyer back">
    <div class="stripe" style="top:0;height:8px"></div>
    <div class="photo" role="img" aria-label="Photo of a therapist's hands examining a patient's lower back"></div>
    <svg class="abs" style="top:350px" width="370" height="320" viewBox="0 0 370 320">
      <path d="M0 18Q185 0 370 18V320H0Z" fill="#1f95d6"/>
      <path d="M0 18Q185 0 370 18" stroke="var(--blue-soft)" stroke-width="3" fill="none"/>
      <path d="M20 312Q185 300 350 312" stroke="var(--blue-pale)" stroke-width="3" fill="none"/>
    </svg>
    <ul class="services">
      <li><span>MANUAL THERAPY,</span></li>
      <li><span>MANUAL LYMPHATIC DRAINAGE,</span></li>
      <li><span>CLASSIC MASSAGE,</span></li>
      <li><span>SECTORAL ALTERNATIVE<br>PRACTITIONERS</span></li>
    </ul>
    <div class="stripe" style="top:668px;height:67px;background:var(--blue-pale)"></div>
    <div class="contact">
      <div><svg viewBox="0 0 8 9"><path d="M4 0A3 3 0 0 1 7 3C7 5 4 9 4 9S1 5 1 3A3 3 0 0 1 4 0Z" fill="var(--blue)"/></svg>WELLENHAFEN, LINDENWEG 17, 04719 TALBRÜCK</div>
      <div><svg viewBox="0 0 8 9"><rect x="0" y="2" width="8" height="5" fill="var(--blue)"/></svg>WELLENHAFEN-PRAXIS-BEISPIEL.DE</div>
    </div>
    <div class="stripe" style="top:735px;height:5px"></div>
  </section>
</body>
</html>
```